QV Pathway Branding
Stationary - Business Card, Letter Head, Powerpoint file, Word Document, Email Signature.
QV Pathway Branding - Information Technology
Creative Brief
Professional
Darren M. L.
Founder
58 Ravel Pine Street #04-12 Orlan Plaza Singapore 142390
darrenm.l@qvpathway-example.com
www.qvpathway-example.com
BRN : 209874163K
The main idea of this contest is not just for the name card but a branding for our stationary. The following are the pointers/comments. I would like it if Icons were used Instead of Phone, Fax, Email, Web. Note: the 2 different Phone numbers in the Cell phone, each should have it's own line if possible. Please use white matte background. For additional effects on the namecard, you may use the different shades to create the effect. For Stationary, please ensure a word document format, powerpoint and email signature format is created as well as the other conventional document types. BRN is only required on the Letterheads. Extra type of formats for branding (e.g. Folder design) earns you extra Stars and ultimately seals the deal with creativity.
Please be creative in the design of the back of the business card. You are to freely manipulate the details given for back and front. Which means you may incorporate in the details in the design to be either the front and or the back.

```html
<!DOCTYPE html>
<html lang="en">
<head>
<meta charset="utf-8">
<title>QV Pathway Branding – Stationery Set</title>
<link href="https://fonts.googleapis.com/css2?family=Open+Sans:wght@400;700&display=swap" rel="stylesheet">
<style>
  :root{
    --red:#e31e24;
    --black:#111111;
    --white:#ffffff;
    --grey:#8a8a8a;
    --ink:#333333;
    --stage:#2b2622;
  }
  *{box-sizing:border-box;margin:0;padding:0}
  html,body{width:1200px;height:869px;overflow:hidden;background:var(--stage)}
  body{position:relative;font-family:"Open Sans",Arial,sans-serif;color:var(--ink)}
  .piece{position:absolute;background:var(--white);overflow:hidden;box-shadow:0 3px 8px rgba(0,0,0,.45)}
  .piece.dark{background:var(--black);color:var(--white)}
  .band{position:absolute;left:0;right:0;background:var(--red)}
  .brand{position:absolute;font-weight:700;color:var(--black);letter-spacing:.02em;white-space:nowrap;display:flex;align-items:center;gap:.3em}
  .brand::after{content:"";width:.55em;height:.55em;background:var(--red);display:inline-block}
  .dark .brand{color:var(--white)}
  .mark-square{position:absolute;border:solid var(--red);opacity:.9}
  .dark .mark-square{border-color:#3a3a3a}
  .small{position:absolute;font-size:6px;line-height:1.45;color:var(--ink);white-space:nowrap}
  .url{position:absolute;font-size:7px;color:var(--white)}
  .slide-title{position:absolute;font-size:17px;line-height:1.15;color:var(--ink)}
</style>
</head>
<body>

<!-- Presentation folder -->
<section class="piece folder" style="left:53px;top:58px;width:417px;height:350px">
  <div class="band" style="top:16px;height:12px"></div>
  <div class="brand" style="left:40px;top:54px;font-size:22px">QV PATHWAY</div>
  <div class="mark-square" style="left:58px;top:170px;width:92px;height:92px;border-width:10px"></div>
  <div class="band" style="top:300px;height:18px;left:0;right:0"></div>
  <div class="url" style="left:170px;top:304px">www.qvpathway-example.com</div>
  <!-- pocket with card -->
  <div class="pocket" style="position:absolute;left:0;top:280px;width:417px;height:70px;background:var(--white);border-top:1px solid #ddd"></div>
  <div class="piece" style="left:30px;top:260px;width:90px;height:52px;border:1px solid #ccc;box-shadow:none">
    <div class="brand" style="left:6px;top:6px;font-size:7px">QV PATHWAY</div>
    <div class="small" style="left:50px;top:24px;font-size:5px;color:var(--red);font-weight:700">Darren M. L.</div>
    <div class="band" style="bottom:3px;height:3px"></div>
  </div>
  <div class="mark-square" style="left:250px;top:300px;width:20px;height:20px;border-width:3px"></div>
</section>

<!-- Folder back panel -->
<section class="piece folder-back" style="left:499px;top:58px;width:163px;height:350px">
  <div class="band" style="top:16px;height:12px"></div>
  <div class="mark-square" style="left:30px;top:110px;width:90px;height:90px;border-width:10px"></div>
  <div class="band" style="bottom:20px;height:12px"></div>
</section>

<!-- Business card front -->
<section class="piece card-front" style="left:679px;top:58px;width:274px;height:153px">
  <div class="band" style="top:10px;height:8px;right:120px"></div>
  <div class="brand" style="left:10px;top:26px;font-size:17px">QV PATHWAY</div>
  <div class="small" style="left:16px;top:54px">T +65 6100 2345<br>M +65 9100 2345<br>M +65 9200 6789<br>F +65 6100 2346<br>darrenm.l@qvpathway-example.com</div>
  <div class="small" style="left:160px;top:60px;font-size:10px;color:var(--red);font-weight:700">Darren M. L.</div>
  <div class="small" style="left:172px;top:76px">Founder</div>
  <div class="mark-square" style="left:222px;top:100px;width:34px;height:34px;border-width:5px"></div>
  <div class="small" style="left:16px;top:132px">www.qvpathway-example.com</div>
</section>

<!-- Business card back -->
<section class="piece dark card-back" style="left:679px;top:216px;width:274px;height:156px">
  <div class="band" style="top:18px;height:6px;right:160px"></div>
  <div class="brand" style="left:30px;top:58px;font-size:20px">QV PATHWAY</div>
  <div class="mark-square" style="left:180px;top:68px;width:60px;height:60px;border-width:8px"></div>
</section>

<!-- Letterhead -->
<section class="piece letterhead" style="left:53px;top:456px;width:290px;height:348px">
  <div class="brand" style="left:16px;top:26px;font-size:18px">QV PATHWAY</div>
  <div class="small" style="left:190px;top:28px;font-size:5px">58 Ravel Pine Street #04-12<br>Orlan Plaza Singapore 142390<br>darrenm.l@qvpathway-example.com<br>www.qvpathway-example.com<br>BRN : 209874163K</div>
  <div class="small" style="left:16px;top:100px;font-size:6px;white-space:normal;width:250px">Dear Client,<br><br>Thank you for your interest in our services. We look forward to working with you on your next project and sharing our plan in detail.<br><br>Please contact us at any time with questions about the proposal or schedule.<br><br>Yours sincerely,<br><br>Darren M. L.</div>
  <div class="mark-square" style="left:196px;top:240px;width:70px;height:70px;border-width:9px"></div>
  <div class="band" style="bottom:10px;height:8px"></div>
  <div class="small" style="left:16px;bottom:22px;font-size:5px">www.qvpathway-example.com</div>
</section>

<!-- Envelope front -->
<section class="piece envelope" style="left:367px;top:475px;width:286px;height:144px">
  <div class="band" style="top:10px;height:8px"></div>
  <div class="brand" style="left:12px;top:26px;font-size:14px">QV PATHWAY</div>
  <div class="mark-square" style="left:220px;top:74px;width:44px;height:44px;border-width:7px"></div>
</section>

<!-- Envelope back -->
<section class="piece envelope-back" style="left:367px;top:629px;width:286px;height:144px">
  <svg width="286" height="144" style="position:absolute;left:0;top:0">
    <path d="M0 0 H286 V16 L143 62 L0 16 Z" fill="var(--black)"/>
  </svg>
  <div class="mark-square" style="left:133px;top:14px;width:20px;height:20px;border-width:3px;border-color:var(--white)"></div>
</section>

<!-- Slide: welcome -->
<section class="piece slide-welcome" style="left:679px;top:379px;width:238px;height:173px">
  <div class="band" style="top:10px;height:8px"></div>
  <div class="brand" style="left:120px;top:24px;font-size:13px">QV PATHWAY</div>
  <div class="slide-title" style="left:12px;top:86px">Welcome to<br>my presentation</div>
  <div class="band" style="bottom:10px;height:6px"></div>
</section>

<!-- Slide: thank you -->
<section class="piece dark slide-thanks" style="left:931px;top:379px;width:211px;height:209px">
  <div class="brand" style="left:14px;top:66px;font-size:15px">QV PATHWAY</div>
  <div class="small" style="left:110px;top:112px;font-size:9px;color:var(--white)">Thank You</div>
  <div class="mark-square" style="left:134px;top:134px;width:56px;height:56px;border-width:8px"></div>
</section>

<!-- Slide: about us -->
<section class="piece slide-about" style="left:679px;top:566px;width:238px;height:192px">
  <div class="band" style="top:12px;height:22px;left:12px;right:12px"></div>
  <div class="small" style="left:26px;top:16px;font-size:11px;color:var(--white)">About Us</div>
  <div role="img" aria-label="Photo of the company team" style="position:absolute;left:14px;top:56px;width:104px;height:66px;background:linear-gradient(180deg,#e8e8e8,#6c6c6c)"></div>
  <div class="small" style="left:128px;top:56px;font-size:5px;white-space:normal;width:100px">We deliver clear IT strategy and dependable systems for growing businesses across the region. Our team works closely with every client.</div>
  <div class="band" style="bottom:10px;height:6px"></div>
</section>

</body>
</html>
```